M25 Billboard Advert Required Please

I need an advert for a motorway Billboard on the M25 , the advert should show the following in big letters:
GUTTER CLEANING
DALRYNFLUES.COM and a small logo off to the side (Our logo is attached)

The printer has requested the following (Important please) the advert has to be
pdf file / 300 dpi/landscape orientation / scaled to a minimum 25% advert size ( this particular site is 22ft x 10ft so 25% of this please). Please also make sure that the artwork is embedded and outlined correctly if this is incorrect it will affect the printing of the banner.

Target Market(s)

General Public

Industry/Entity Type

Gutter Cleaning

Requirements
Should not have
• No Change to our Logo

```html
<!DOCTYPE html>
<html lang="en">
<head>
<meta charset="utf-8">
<title>Gutter Cleaning – Dalryn Flues Billboard</title>
<link rel="stylesheet" href="https://fonts.googleapis.com/css2?family=Anton&family=Archivo+Black&family=Open+Sans:wght@700&display=swap">
<style>
  :root {
    --paper: #ffffff;
    --headline-red: #b91f28;
    --ink: #231f20;
    --band-dark: #3d0004;
    --band-mid: #8a0308;
    --band-bright: #e31b23;
  }
  html, body {
    margin: 0;
    padding: 0;
    width: 866px;
    height: 1200px;
    overflow: hidden;
    background: var(--paper);
  }
  .canvas {
    width: 866px;
    height: 1200px;
    display: flex;
    align-items: center;
    justify-content: center;
  }
  .billboard {
    display: block;
    width: 866px;
    height: 394px;
  }
  .headline {
    font-family: "Anton", "Oswald", sans-serif;
    fill: var(--headline-red);
  }
  .web-address {
    font-family: "Archivo Black", "Arial Black", sans-serif;
    fill: var(--ink);
  }
  .brand-name {
    font-family: "Archivo Black", "Arial Black", sans-serif;
    fill: var(--ink);
  }
  .brand-tagline {
    font-family: "Open Sans", Arial, sans-serif;
    font-weight: 700;
    fill: var(--ink);
  }
</style>
</head>
<body>
<div class="canvas">
  <svg class="billboard" viewBox="0 0 1420 645.5" preserveAspectRatio="none" xmlns="http://www.w3.org/2000/svg">
    <defs>
      <linearGradient id="top-band-fade" x1="0" y1="0" x2="1" y2="0">
        <stop offset="0" stop-color="var(--band-dark)"/>
        <stop offset="0.55" stop-color="var(--band-mid)"/>
        <stop offset="1" stop-color="var(--band-bright)"/>
      </linearGradient>
      <linearGradient id="side-band-fade" x1="0" y1="0" x2="0" y2="1">
        <stop offset="0" stop-color="#c0141b"/>
        <stop offset="1" stop-color="#7a0006"/>
      </linearGradient>
      <linearGradient id="mound-fade" x1="0" y1="0" x2="1" y2="1">
        <stop offset="0" stop-color="var(--band-bright)"/>
        <stop offset="0.55" stop-color="#a8070e"/>
        <stop offset="1" stop-color="#4a0003"/>
      </linearGradient>
    </defs>

    <rect class="panel" width="1420" height="645.5" fill="var(--paper)"/>

    <path class="top-band" d="M0,0 H1420 V78 L710,39 L0,78 Z" fill="url(#top-band-fade)"/>

    <path class="bottom-band-left" d="M0,566 L340,581 L340,645.5 L0,645.5 Z" fill="url(#side-band-fade)"/>
    <path class="bottom-band-right" d="M1080,581 L1420,566 L1420,645.5 L1080,645.5 Z" fill="url(#side-band-fade)"/>
    <path class="bottom-mound" d="M250,645.5 C250,600 290,566 340,563 L715,534 L1060,563 C1130,567 1180,603 1180,645.5 Z" fill="url(#mound-fade)"/>

    <text class="headline" x="60" y="381" font-size="280" textLength="1300" lengthAdjust="spacingAndGlyphs">GUTTER CLEANING</text>

    <g class="brand-mark">
      <rect class="brand-square" x="140" y="428" width="28" height="28" fill="var(--headline-red)"/>
      <text class="brand-name" x="176" y="452" font-size="24" textLength="160" lengthAdjust="spacingAndGlyphs">Dalryn Flues</text>
      <text class="brand-tagline" x="140" y="477" font-size="11" textLength="196" lengthAdjust="spacingAndGlyphs">Clean gutters protect your property</text>
    </g>

    <text class="web-address" x="375" y="484" font-size="84" textLength="920" lengthAdjust="spacingAndGlyphs">DALRYNFLUES.COM</text>
  </svg>
</div>
</body>
</html>
```